New business card design needed for Trucking/Staffing company!

I am looking for a business card design. The business name is Harbor Lane Freightworks, LLC. This company is a staffing company for commercial drivers/truck drivers. Most of our customers are trucking/supply companies. Our colors are blue/black/white/grey. The info I have on my current business cards is
-Spot for a name
-2 lines for an address
-3 lines for Office, cell, and fax
-email
-website(currently on backside of card with logo but can go anywhere)
Updates

Project Deadline Extended
Reason: Open to more designs

Target Market(s)

Trucking companies, building supply companies

Industry/Entity Type

Business

Contact Information for Business Card

Edgy but professional

Font styles to use
Other font styles liked:
• Open to suggestions

Colors
0555a3
000000
ffffff
9d9d9d

Requirements
Must have
• Must have the logo incorporated

```html
<!DOCTYPE html>
<html lang="en">
<head>
<meta charset="utf-8">
<title>Harbor Lane Freightworks, LLC — Business Card</title>
<link rel="stylesheet" href="https://fonts.googleapis.com/css2?family=Open+Sans:wght@400;600;700&display=swap">
<style>
  :root {
    --navy: #383a87;
    --navy-deep: #2f317a;
    --ink: #2b2b2b;
    --ink-soft: #3c3c3c;
    --white: #ffffff;
    --silver-light: #f7f7f7;
    --silver-mid: #dcdcdc;
    --silver-dark: #b9b9b9;
    --page: #eeeeee;
  }
  * { margin: 0; padding: 0; box-sizing: border-box; }
  html, body {
    width: 1130px; height: 1200px; overflow: hidden;
    background: var(--page);
    font-family: "Open Sans", Arial, sans-serif;
  }
  .sheet { position: relative; width: 1130px; height: 1200px; }

  .card {
    position: absolute; left: 151px; width: 828px; height: 480px;
    overflow: hidden;
    background: linear-gradient(100deg, var(--silver-dark) 0%, var(--silver-mid) 22%, var(--silver-light) 50%, var(--white) 60%, var(--silver-mid) 85%, var(--silver-dark) 100%);
    box-shadow: 0 2px 6px rgba(0,0,0,.18);
  }
  .card--front { top: 80px; }
  .card--back { top: 630px; }
  .card__band { position: absolute; left: 0; top: 0; width: 828px; height: 480px; }

  .brand-name {
    position: absolute; left: 0; width: 100%; text-align: center;
    font-weight: 700; letter-spacing: 1px; text-transform: uppercase;
    white-space: nowrap;
  }
  .card--front .brand-name { top: 150px; font-size: 40px; color: var(--navy); }
  .card--back .brand-name { top: 58px; font-size: 28px; color: var(--white); }

  .website {
    position: absolute; left: 0; width: 100%; top: 380px; text-align: center;
    color: var(--white); font-size: 28px; font-weight: 600;
  }

  .contact { position: absolute; left: 214px; top: 182px; color: var(--ink); }
  .contact__name { font-size: 30px; font-weight: 700; line-height: 40px; }
  .contact__position { font-size: 26px; color: var(--ink-soft); line-height: 36px; margin-bottom: 16px; }
  .contact__list { list-style: none; }
  .contact__item { position: relative; padding-left: 34px; font-size: 22px; line-height: 32.5px; color: var(--ink-soft); }
  .contact__icon { position: absolute; left: 0; top: 7px; width: 22px; height: 22px; }
  .contact__item--plain { padding-left: 34px; }

  .brand-mark-faint {
    position: absolute; right: 40px; bottom: 50px; width: 150px; height: 150px;
    border-radius: 50%; background: rgba(56,58,135,.08);
  }
</style>
</head>
<body>
<main class="sheet">

  <section class="card card--front" aria-label="Card front">
    <svg class="card__band" viewBox="0 0 828 480" preserveAspectRatio="none" aria-hidden="true">
      <defs>
        <linearGradient id="rimFront" x1="0" x2="1">
          <stop offset="0" stop-color="#9a9a9a"/>
          <stop offset=".5" stop-color="#ffffff"/>
          <stop offset="1" stop-color="#8f8f8f"/>
        </linearGradient>
      </defs>
      <path d="M0 330 Q414 300 828 330 L828 480 L0 480 Z" fill="url(#rimFront)"/>
      <path d="M0 338 Q414 310 828 338 L828 480 L0 480 Z" fill="var(--navy)"/>
    </svg>
    <div class="brand-name">Harbor Lane Freightworks, LLC</div>
    <div class="website">www.harborlanefreightworks.com</div>
  </section>

  <section class="card card--back" aria-label="Card back">
    <svg class="card__band" viewBox="0 0 828 480" preserveAspectRatio="none" aria-hidden="true">
      <defs>
        <linearGradient id="rimBack" x1="0" x2="1">
          <stop offset="0" stop-color="#9a9a9a"/>
          <stop offset=".5" stop-color="#ffffff"/>
          <stop offset="1" stop-color="#8f8f8f"/>
        </linearGradient>
      </defs>
      <path d="M0 0 L828 0 L828 136 Q414 164 0 136 Z" fill="url(#rimBack)"/>
      <path d="M0 0 L828 0 L828 128 Q414 156 0 128 Z" fill="var(--navy)"/>
    </svg>
    <div class="brand-name">Harbor Lane Freightworks, LLC</div>

    <div class="brand-mark-faint" aria-hidden="true"></div>

    <div class="contact">
      <div class="contact__name">Your Name</div>
      <div class="contact__position">Position</div>
      <ul class="contact__list">
        <li class="contact__item">
          <svg class="contact__icon" viewBox="0 0 24 24" aria-hidden="true"><path d="M6.6 2.5 9.4 6.8 7.6 8.7c1.3 2.9 3.6 5.2 6.6 6.7l1.8-1.9 4.4 2.7-1.3 3.5c-.4.8-1.2 1.2-2 1C9.6 19.3 4.7 14.4 3 7a1.9 1.9 0 0 1 1-2.1Z" fill="none" stroke="var(--ink)" stroke-width="2" stroke-linejoin="round"/></svg>
          123-456-7890
        </li>
        <li class="contact__item">
          <svg class="contact__icon" viewBox="0 0 24 24" aria-hidden="true"><rect x="6" y="2" width="12" height="20" rx="2" fill="none" stroke="var(--ink)" stroke-width="2"/><line x1="10" y1="18.5" x2="14" y2="18.5" stroke="var(--ink)" stroke-width="2"/></svg>
          123-456-7888
        </li>
        <li class="contact__item">
          <svg class="contact__icon" viewBox="0 0 24 24" aria-hidden="true"><rect x="2" y="6" width="20" height="13" fill="none" stroke="var(--ink)" stroke-width="2"/><path d="M2 6 12 14 22 6" fill="none" stroke="var(--ink)" stroke-width="2"/></svg>
          name@companyname.com
        </li>
        <li class="contact__item">
          <svg class="contact__icon" viewBox="0 0 24 24" aria-hidden="true" style="top:20px"><path d="M12 23s-7-8.2-7-13a7 7 0 0 1 14 0c0 4.8-7 13-7 13Z" fill="var(--ink)"/><circle cx="12" cy="10" r="2.8" fill="var(--white)"/></svg>
          Address
        </li>
        <li class="contact__item contact__item--plain">Address</li>
      </ul>
    </div>
  </section>

</main>
</body>
</html>
```